High Tech Software Startup needs Letterhead Design

We need a letterhead for a startup company base in Brazil. The letterhead should combine with our logo attached here.
We are a team of professionals in Java for web and mobile with iOS and android development.
We are looking for a modern and futuristc design.

Target Market(s)

CIO, IT managers of mid to big size companies

Industry/Entity Type

It Company

```html
<!DOCTYPE html>
<html lang="en">
<head>
<meta charset="utf-8">
<title>Voltra Stationery</title>
<link href="https://fonts.googleapis.com/css2?family=Montserrat:wght@400;600;700&display=swap" rel="stylesheet">
<style>
  :root {
    --navy: #27406b;
    --navy-deep: #1f3560;
    --blue: #1f8fd0;
    --ink: #3a3f47;
    --muted: #6c727b;
    --rule: #d6d9dd;
    --paper: #ffffff;
    --bg: #eef0f2;
  }
  * { box-sizing: border-box; margin: 0; padding: 0; }
  html, body { width: 1200px; height: 979px; overflow: hidden; }
  body {
    background: var(--bg);
    font-family: "Montserrat", Arial, sans-serif;
    color: var(--ink);
    position: relative;
  }
  .frame-svg { position: absolute; inset: 0; width: 100%; height: 100%; }

  .brand {
    display: flex; align-items: center; gap: 8px;
    font-weight: 700; color: var(--navy); letter-spacing: 0.5px;
    position: relative;
  }
  .brand-square { background: var(--blue); display: inline-block; }

  /* Letterhead */
  .letterhead {
    position: absolute; left: 110px; top: 60px;
    width: 560px; height: 792px;
    background: var(--paper);
    box-shadow: 0 2px 8px rgba(0,0,0,0.08);
  }
  .letterhead .brand { position: absolute; left: 52px; top: 58px; font-size: 30px; }
  .letterhead .brand-square { width: 26px; height: 26px; }
  .letterhead-footer {
    position: absolute; right: 44px; bottom: 46px;
    display: flex; gap: 14px; font-size: 7.5px; line-height: 1.5; color: var(--muted);
  }
  .footer-col { padding-left: 14px; border-left: 1px solid var(--rule); }
  .footer-col:first-child { border-left: none; padding-left: 0; }
  .label { color: var(--blue); font-weight: 600; }

  /* Business cards */
  .card {
    position: absolute; left: 730px; width: 380px; height: 218px;
    box-shadow: 0 2px 8px rgba(0,0,0,0.1);
  }
  .card-front { top: 300px; background: var(--paper); }
  .card-back { top: 590px; background: linear-gradient(135deg, var(--navy) 0%, var(--navy-deep) 100%); }
  .card-front .brand { position: absolute; left: 34px; top: 42px; font-size: 26px; }
  .card-front .brand-square { width: 22px; height: 22px; }
  .card-address {
    position: absolute; left: 34px; bottom: 40px;
    font-size: 7.5px; line-height: 1.5; color: var(--muted);
  }
  .card-person {
    position: absolute; right: 36px; top: 44px; text-align: right;
    font-size: 7.5px; line-height: 1.6; color: var(--muted);
  }
  .person-name { font-weight: 700; color: var(--navy); font-size: 9px; letter-spacing: 0.4px; }
  .person-role { color: var(--blue); margin-bottom: 8px; }
  .contact-line { display: flex; justify-content: flex-end; align-items: center; gap: 5px; }
  .contact-line svg { width: 8px; height: 8px; }
  .card-back .brand {
    position: absolute; left: 50%; top: 50%; transform: translate(-50%, -50%);
    font-size: 28px; color: #ffffff;
  }
  .card-back .brand-square { width: 24px; height: 24px; background: #ffffff; }
</style>
</head>
<body>

<section class="letterhead">
  <svg class="frame-svg" viewBox="0 0 560 792" aria-hidden="true">
    <defs>
      <linearGradient id="lhAccent" x1="0" y1="0" x2="0" y2="1">
        <stop offset="0" stop-color="#27406b"/>
        <stop offset="1" stop-color="#1f8fd0"/>
      </linearGradient>
    </defs>
    <rect x="22" y="22" width="514" height="748" rx="14" fill="none" stroke="#d6d9dd" stroke-width="1"/>
    <path d="M518 22 Q538 22 538 42 L538 752 Q538 772 518 772 L200 772" fill="none" stroke="url(#lhAccent)" stroke-width="5"/>
  </svg>
  <div class="brand"><span class="brand-square"></span>VOLTRA</div>
  <footer class="letterhead-footer">
    <div class="footer-col">Rua Alvorada Nova 418 · 9o andar<br>Centro · Campinas · SP</div>
    <div class="footer-col"><span class="label">Phone:</span> +55 19 3412 5580<br><span class="label">Fax:</span> +55 19 3412 5581</div>
    <div class="footer-col">hello@voltra.dev<br>www.voltra.dev</div>
  </footer>
</section>

<section class="card card-front">
  <svg class="frame-svg" viewBox="0 0 380 218" aria-hidden="true">
    <polygon points="30,14 350,14 366,30 366,188 350,204 30,204 14,188 14,30" fill="none" stroke="#d6d9dd" stroke-width="1"/>
    <path d="M350 14 L366 30 L366 188 L350 204 L200 204" fill="none" stroke="#1f8fd0" stroke-width="3"/>
  </svg>
  <div class="brand"><span class="brand-square"></span>VOLTRA</div>
  <div class="card-address">Rua Alvorada Nova 418<br>9o andar · Centro</div>
  <div class="card-person">
    <div class="person-name">LUCAS MOREIRA</div>
    <div class="person-role">managing director</div>
    <div class="contact-line">
      <svg viewBox="0 0 10 10"><rect x="2" y="0.5" width="6" height="9" rx="1" fill="#1f8fd0"/></svg>
      +55 19 98120 4433
    </div>
    <div class="contact-line">
      <svg viewBox="0 0 10 10"><rect x="0.5" y="2" width="9" height="6" rx="1" fill="#1f8fd0"/><path d="M0.5 2 L5 5.5 L9.5 2" fill="none" stroke="#fff" stroke-width="0.8"/></svg>
      hello@voltra.dev
    </div>
  </div>
</section>

<section class="card card-back">
  <svg class="frame-svg" viewBox="0 0 380 218" aria-hidden="true">
    <polygon points="30,14 350,14 366,30 366,188 350,204 30,204 14,188 14,30" fill="none" stroke="#4f73a8" stroke-width="1"/>
    <path d="M366 150 L366 188 L350 204 L230 204" fill="none" stroke="#1f8fd0" stroke-width="3"/>
  </svg>
  <div class="brand"><span class="brand-square"></span>VOLTRA</div>
</section>

</body>
</html>
```